The Quiet Ascent Book Cover

Book Title:
The Quiet Ascent: Lessons of Insight From A Circle of Mentors to Guide You Toward a Fuller Journey

This book will offer the wisdom and philosophies of a variety of different coaches to allow future clients to get a taste of you and your style and prepare them to work with you!

A coach does not fix you. Or heal you. They coach you - offer thoughts to ponder, guidance, techniques to try. All to help you plays and succeed at the game of life.

Each coach has their own personality, training, experience, method and philosophy they bring to the table. The underlying purpose is to guide you through The Quiet Ascent, to become the person you desire and aspire to be. Different coaches for different folks, yet they all have their own unique wisdom and special sauce to share.

This book is a collection of just that. A tasting of the wisdom and philosophies of a variety of different coaches for you to experience.

Types of Coaches: Clarity, Dreams, Goals, Motivation, Mindset,  Subconscious, Beliefs, Behavior, Accountability, Life, Wellness, Love & Dating, Relationships, Sex, Business, Career,  Executive,  Personal Development,  Writing, Wellness, Fitness, Parenting,  Style, Spirituality, Public Speaking, Financial,  Time management, Weight Loss, Running, Self esteem,  Tarot, Astrology, Enneagram, Soul path/ Dharma, Skills, Performance,  Speaking / Communication, Leadership, Shadow Work, Acting, Sports, ANY & ALL

Target Market(s)

Males or females looking for guidance and words of wisdom from an expert coach - maybe to find one that resonates with them to work with further. Ages 16 and up. Any Gender. International. Looking to improve their life!

Industry/Entity Type

Self Development, Wellness, Coaching, Personal Growth, Fitness, Spirituality, Business, Relationships

Font styles to use
Serif
Script

Colors
0054AA
0677BA
7BADD7
CADEEF
E8F1F8
FFF300
FFF600
FEFA6F
FFFEC7
FFFEE8

Requirements
Must have
• I am looking for a visually appealing, unique cover that encompasses the breadth and depth of the transformation that people can go through and inspires them to want to grow and change even more. I love when elegant and classic simplicity is combined with some kind of twist that catches the eye and provokes thought. I love complimentary fonts, colors, design elements. You can visit my Veltrano Author Page - Dr. Marisol Penbury Aldane to see my titles to see what I have liked! But I am also excited to see where you can make my vision even better!!
Nice to have
• Front Cover - Image, Title and Subtitle, The Lark Publishing House, Spine - Title and Publishing House Logo, Back - Book Blurb, Authors Names, Info about Publishing House, ISBN Barcode
Should not have
• Anything too feminine or too masculine as I want to encourage coaches of all genders to participate.

```html
<!DOCTYPE html>
<html lang="en">
<head>
<meta charset="utf-8">
<title>The Quiet Ascent – Book Cover</title>
<link rel="stylesheet" href="https://fonts.googleapis.com/css2?family=Archivo:wght@600;700;800&display=swap">
<style>
  :root {
    --backdrop: #3a3a3c;
    --cover-white: #fdfdff;
    --ink-title: #262628;
    --ink-subtitle: #1f2f6e;
    --ink-publisher: #2a3a7c;
    --ring-blue: #b9d6ee;
    --ring-teal: #7fc2d8;
    --ring-violet: #a99ad8;
    --ring-rose: #e07a8a;
  }
  * { margin: 0; padding: 0; box-sizing: border-box; }
  html, body {
    width: 882px;
    height: 1200px;
    overflow: hidden;
    background: var(--backdrop);
  }
  .canvas {
    position: relative;
    width: 882px;
    height: 1200px;
  }
  .book-cover {
    position: absolute;
    left: 91px;
    top: 42px;
    width: 700px;
    height: 1116px;
    background: var(--cover-white);
    overflow: hidden;
    font-family: "Archivo", "Helvetica Neue", Arial, sans-serif;
  }
  .butterfly-swirl {
    position: absolute;
    inset: 0;
    background:
      radial-gradient(ellipse 62% 46% at 42% 44%,
        rgba(255,255,255,0) 0%,
        rgba(255,255,255,0) 52%,
        rgba(185,214,238,0.55) 64%,
        rgba(127,194,216,0.45) 74%,
        rgba(169,154,216,0.38) 84%,
        rgba(224,122,138,0.32) 94%,
        rgba(255,255,255,0) 100%);
  }
  .cover-text {
    position: absolute;
    left: 0;
    right: 0;
    top: 365px;
    text-align: center;
  }
  .title {
    color: var(--ink-title);
    font-weight: 800;
    font-size: 78px;
    line-height: 76px;
    letter-spacing: -0.5px;
  }
  .title span { display: block; }
  .subtitle {
    margin: 30px auto 0;
    width: 540px;
    color: var(--ink-subtitle);
    font-weight: 700;
    font-size: 23px;
    line-height: 31px;
  }
  .publisher {
    position: absolute;
    left: 0;
    right: 0;
    bottom: 44px;
    text-align: center;
    color: var(--ink-publisher);
    font-weight: 700;
    font-size: 27px;
    letter-spacing: 0.5px;
    text-transform: uppercase;
  }
</style>
</head>
<body>
  <main class="canvas">
    <section class="book-cover">
      <div class="butterfly-swirl" role="img" aria-label="Swirl of butterflies in blue, violet and rose circling the title"></div>
      <div class="cover-text">
        <h1 class="title"><span>The</span><span>Quiet</span><span>Ascent</span></h1>
        <p class="subtitle">Lessons of Insight From A Circle of Mentors to Guide You Toward a Fuller Journey</p>
      </div>
      <p class="publisher">The Lark Publishing House</p>
    </section>
  </main>
</body>
</html>
```